Feng Shui Consultant needing a business card designed

please incorporate the following colours in the design: lilac (primarily)black and gold
Name of the business is: Harbour Feng Shui
The main design should incorporate a willow tree, to be the main focus of the design
The design should be modern and sophisticated
The back of the card should include the following details;
name; Marguerite Dolan
title: Accredited Feng Shui Consultant
phone number; 0457 392 815
email address; marguerite_dolan@quillmail.net
Specialising in Feng Shui and Space Clearing

Target Market(s)

Highend, affluent white collar clients. Well educated

Industry/Entity Type

Business

Colors
e3daeb

```html
<!DOCTYPE html>
<html lang="en">
<head>
<meta charset="utf-8">
<title>Harbour Feng Shui – Business Card</title>
<link rel="stylesheet" href="https://fonts.googleapis.com/css2?family=Jost:wght@300;400;500&display=swap">
<style>
  :root {
    --backdrop: #d9d9d9;
    --peach: #f59a7e;
    --coral: #ec6f86;
    --magenta: #e0478c;
    --plum: #7a1d57;
    --orchid: #c259a8;
    --blush: #f2a3bd;
    --ink: #1a0f16;
    --paper: #ffffff;
  }
  * { box-sizing: border-box; margin: 0; padding: 0; }
  html, body {
    width: 1200px; height: 900px; overflow: hidden;
    background: var(--backdrop);
    font-family: "Jost", "Futura", sans-serif;
  }
  .stage { position: relative; width: 1200px; height: 900px; }

  .card {
    position: absolute;
    width: 630px; height: 360px;
    overflow: hidden;
    box-shadow: 0 10px 28px rgba(0,0,0,0.25);
    background:
      radial-gradient(ellipse 45% 45% at 85% 12%, var(--blush) 0%, transparent 70%),
      radial-gradient(ellipse 55% 45% at 42% 0%, var(--plum) 0%, transparent 75%),
      radial-gradient(ellipse 50% 55% at 8% 92%, var(--peach) 0%, transparent 75%),
      radial-gradient(ellipse 50% 50% at 70% 85%, var(--orchid) 0%, transparent 75%),
      linear-gradient(120deg, var(--peach) 0%, var(--coral) 30%, var(--magenta) 55%, var(--orchid) 100%);
  }
  .card--front { left: 140px; top: 70px; }
  .card--back  { left: 430px; top: 470px; }

  .brand {
    display: flex; flex-direction: column; align-items: center; gap: 16px;
    font-weight: 300; letter-spacing: 0.02em; text-transform: uppercase;
  }
  .brand__dot { width: 34px; height: 34px; border-radius: 50%; }
  .card--front .brand {
    position: absolute; left: 0; right: 0; top: 110px;
    color: var(--paper); font-size: 28px;
  }
  .card--front .brand__dot { background: var(--paper); }

  .card--back .brand {
    position: absolute; left: 30px; top: 60px;
    color: var(--ink); font-size: 26px; align-items: flex-start;
  }
  .card--back .brand__dot { background: var(--ink); margin-left: 170px; }

  .contact {
    position: absolute; left: 330px; top: 118px; width: 280px; color: var(--ink);
  }
  .contact__name {
    font-size: 21px; font-weight: 500; letter-spacing: 0.12em; text-transform: uppercase;
  }
  .contact__title {
    font-size: 10.5px; font-weight: 500; letter-spacing: 0.06em; text-transform: uppercase;
    padding-bottom: 6px; border-bottom: 1.5px dotted var(--ink);
  }
  .contact__list { list-style: none; margin-top: 8px; }
  .contact__item {
    display: flex; align-items: center; gap: 8px; font-size: 13px; line-height: 22px;
  }
  .contact__item svg { width: 14px; height: 14px; flex: none; }
  .contact__item--web { padding-bottom: 6px; border-bottom: 1.5px dotted var(--ink); }
  .contact__address { font-size: 14px; margin-top: 8px; }
</style>
</head>
<body>
<main class="stage">

  <section class="card card--front" aria-label="Card front">
    <div class="brand">
      <span class="brand__dot"></span>
      <span class="brand__name">Harbour Feng Shui</span>
    </div>
  </section>

  <section class="card card--back" aria-label="Card back">
    <div class="brand">
      <span class="brand__dot"></span>
      <span class="brand__name">Harbour Feng Shui</span>
    </div>

    <div class="contact">
      <h1 class="contact__name">Marguerite Dolan</h1>
      <p class="contact__title">Accredited Feng Shui Consultant</p>
      <ul class="contact__list">
        <li class="contact__item">
          <svg viewBox="0 0 16 16" aria-hidden="true"><path d="M4 1.5l2.3 3-1.4 1.6c.8 1.9 2.2 3.3 4.1 4.2l1.6-1.4 3 2.3-1.3 2.6C7 13.4 2.6 9 1.6 3z" fill="#1a0f16"/></svg>
          <span>: 0457 392 815</span>
        </li>
        <li class="contact__item">
          <svg viewBox="0 0 16 16" aria-hidden="true"><rect x="1" y="3" width="14" height="10" fill="none" stroke="#1a0f16" stroke-width="1.3"/><path d="M1 3l7 6 7-6" fill="none" stroke="#1a0f16" stroke-width="1.3"/></svg>
          <span>: marguerite_dolan@quillmail.net</span>
        </li>
        <li class="contact__item contact__item--web">
          <svg viewBox="0 0 16 16" aria-hidden="true"><circle cx="8" cy="8" r="6.5" fill="none" stroke="#1a0f16" stroke-width="1.3"/><ellipse cx="8" cy="8" rx="3" ry="6.5" fill="none" stroke="#1a0f16" stroke-width="1.1"/><path d="M1.5 8h13" stroke="#1a0f16" stroke-width="1.1"/></svg>
          <span>: www.harbourfengshui.net</span>
        </li>
      </ul>
      <p class="contact__address">Calle Serena #6 Bahía Norte 3</p>
    </div>
  </section>

</main>
</body>
</html>
```